New Business card design to reflect rebrand

I would like a business card design with a good base colour for our new logo and also a placeholder for a profile pic of the card holder. the design needs to be editable to the point that we can easily change the picture of the person and use that design for printlarkly etc. we are looking at a metalic finish business card so will need a good base colour to bring out the finish.

Target Market(s)

prospective customers

Industry/Entity Type

Business

Contact Information for Business Card

I would like one editable design that we can change the name of the card holder and profile picture. The design need to be in a format that be send to printlarkly etc.

Our address is Fenwick Lodge, Mill Lane, Ashcombe Green, KT14 3WB Tel no. 01632 960418

Requirements
Must have
• place holder for a profile pic for the card holder. in AI or preferably PSD format

```html
<!DOCTYPE html>
<html lang="en">
<head>
<meta charset="utf-8">
<title>Brantwell Workplace Services – Business Card</title>
<link rel="stylesheet" href="https://fonts.googleapis.com/css2?family=Open+Sans:wght@400;600&display=swap">
<style>
  :root{
    --slate:#44576f;
    --orange:#ec6627;
    --paper:#ffffff;
    --backdrop:#e9e7e4;
    --ink:#44576f;
    --photo-light:#eceef0;
    --photo-dark:#1f2838;
  }
  *{box-sizing:border-box;margin:0;padding:0}
  html,body{width:1200px;height:1200px;overflow:hidden;background:var(--backdrop)}
  body{position:relative;font-family:"Open Sans",sans-serif;color:var(--ink)}

  .card{position:absolute;box-shadow:0 6px 18px rgba(0,0,0,.18)}
  .card-front{left:182px;top:70px;width:837px;height:474px;background:var(--paper);overflow:hidden}
  .card-back{left:198px;top:674px;width:804px;height:440px;background:var(--slate);display:flex;align-items:center;justify-content:center}

  .brand{position:absolute;left:40px;top:66px;width:300px;text-align:center;color:var(--slate);font-weight:600;line-height:1.15}
  .brand-name{font-size:40px;letter-spacing:1px}
  .brand-sub{font-size:17px;letter-spacing:3px}

  .holder-bar{position:absolute;left:0;top:207px;width:15px;height:59px;background:var(--slate)}
  .holder-name{position:absolute;left:32px;top:204px;font-size:29px;color:var(--orange);font-weight:400}
  .holder-title{position:absolute;left:32px;top:241px;font-size:19px;color:var(--slate)}

  .contacts{position:absolute;left:32px;top:289px;list-style:none;font-size:19px;line-height:28px;color:var(--slate)}
  .contacts li{display:flex;align-items:center;gap:10px}
  .contacts svg{width:17px;height:17px;flex:none}

  .address{position:absolute;left:32px;top:388px;font-size:19px;line-height:28px;color:var(--slate);font-style:normal}

  .bottom-band{position:absolute;left:0;bottom:0;width:640px;height:16px;background:var(--slate)}
  .bottom-accent{position:absolute;left:598px;bottom:0;width:40px;height:16px;background:var(--orange);clip-path:polygon(0 0,22px 0,100% 100%,9px 100%)}

  .profile-photo{position:absolute;inset:0;background:linear-gradient(160deg,var(--photo-light) 0%,#c9ccd1 35%,var(--photo-dark) 70%);clip-path:polygon(536px 0,837px 0,837px 474px,626px 474px,536px 322px)}

  .back-name{color:#fff;font-size:58px;font-weight:600;letter-spacing:4px}
</style>
</head>
<body>
  <section class="card card-front">
    <div class="brand">
      <div class="brand-name">BRANTWELL</div>
      <div class="brand-sub">WORKPLACE SERVICES</div>
    </div>

    <div class="holder-bar"></div>
    <h1 class="holder-name">Daniel Hartwell</h1>
    <p class="holder-title">Managing Parter</p>

    <ul class="contacts">
      <li>
        <svg viewBox="0 0 20 20" aria-hidden="true"><path fill="#ec6627" d="M2 8c0-3 4-5 8-5s8 2 8 5l-4 1-1-2H7L6 9 2 8zm4 3h8l2 6H4z"/><circle cx="10" cy="14" r="1.6" fill="#fff"/></svg>
        01632 960418
      </li>
      <li>
        <svg viewBox="0 0 20 20" aria-hidden="true"><rect x="1" y="4" width="18" height="12" fill="#ec6627"/><path d="M1 4l9 7 9-7" fill="none" stroke="#fff" stroke-width="1.4"/></svg>
        dhartwell@brantwellwork.com
      </li>
      <li>
        <svg viewBox="0 0 20 20" aria-hidden="true" fill="none" stroke="#ec6627" stroke-width="1.4"><circle cx="10" cy="10" r="8"/><ellipse cx="10" cy="10" rx="3.5" ry="8"/><path d="M2 10h16M3.5 6h13M3.5 14h13"/></svg>
        www.brantwellwork.com
      </li>
    </ul>

    <address class="address">
      Fenwick Lodge, Mill Lane<br>
      Ashcombe Green, KT14 3WB
    </address>

    <div class="bottom-band"></div>
    <div class="bottom-accent"></div>
    <div class="profile-photo" role="img" aria-label="Profile photo placeholder for the card holder"></div>
  </section>

  <section class="card card-back">
    <div class="back-name">BRANTWELL</div>
  </section>
</body>
</html>
```